Buchcover für rechtliche Unterstützung von Verantwortungsträgern in Druckereien zum Thema Reklamation
Super engagiert , ging auch auf Sonderwünsche ein und hat einen fantastischen Support gegeben.
Zielgruppe
Wir unterstützen deutschlandweit all diejenigen Verantwortungsträger in Druckereien die bei einer späteren Reklamation von Kunden und Liefernatenverträgen den Kopf hinhalten müssen , indem wir mit unserem System die Sinne für 90% aller im Alltag vorkommenden Vertragsfallen schärfen.
Aufgabenstellung
Titel : Rechtzeitig klug handeln
SL : Einige etwas andere Blicke auf Verträge und Versicherungen der Druckindustrie. Eine Pflichtlektüre für Verantwortliche im Vertrieb und Einkauf und QM des Etiketten- ,und Verpackungsdrucks
Zielgruppe sind Verantwortungsträger in Druckereien wie Einkauf , Vertrieb, Qualitätsmanagement , Geschäftsleitung ( Männer und Frauen gleichermaßen ) eher konservativ , technikorientiert
Vielen Dank für die tollen Vorschläge. Meine Idee war aber mich als Experten zu positionieren . Das Buichg soll auch somit einen Wiedererkennungseffekt bilden. Ich habe einbmal amn Wochenende gesammelt und mich einmal selbst am Layout versucht.

```html
<!DOCTYPE html>
<html lang="de">
<head>
<meta charset="utf-8">
<title>Rechtzeitig klug handeln – Buchcover</title>
<link rel="stylesheet" href="https://fonts.googleapis.com/css2?family=Anton&family=Roboto:ital,wght@0,400;0,500;0,700;1,400;1,700&family=Roboto+Condensed:wght@700&display=swap">
<style>
  :root {
    --bg: #e9e7e3;
    --cover: #1b1b1b;
    --cover-light: #2a2a2a;
    --spine: #151515;
    --yellow: #f6b80c;
    --white: #ffffff;
    --text-soft: #d8d8d8;
    --panel: #101010;
  }
  * { margin: 0; padding: 0; box-sizing: border-box; }
  html, body { width: 1200px; height: 800px; overflow: hidden; background: var(--bg); }
  .canvas { position: relative; width: 1200px; height: 800px; }
  .book { position: absolute; left: 80px; top: 40px; width: 1040px; height: 720px; display: flex; box-shadow: 0 10px 30px rgba(0,0,0,.25); }

  /* back cover */
  .back-cover { position: relative; width: 490px; height: 720px; background: radial-gradient(ellipse at 50% 40%, var(--cover-light), var(--cover) 75%); color: var(--text-soft); font-family: "Roboto", sans-serif; }
  .back-panel { position: absolute; left: 150px; top: 130px; width: 300px; height: 520px; background: var(--panel); opacity: .85; }
  .author-portrait-small { position: absolute; left: 80px; top: 90px; width: 120px; height: 150px; background: linear-gradient(180deg, #cfcfcf 0%, #8d8d8d 45%, #1e1e1e 100%); }
  .brand-name { position: absolute; left: 212px; top: 208px; font-family: "Roboto", sans-serif; font-weight: 700; font-size: 24px; line-height: 1; color: var(--white); letter-spacing: .5px; }
  .back-text { position: absolute; left: 166px; top: 256px; width: 270px; font-size: 10.5px; line-height: 1.4; }
  .back-text p { margin-bottom: 13px; }

  /* spine */
  .spine { position: relative; width: 60px; height: 720px; background: var(--spine); border-left: 1px solid #000; border-right: 1px solid #000; }
  .spine-subtitle { position: absolute; left: 8px; top: 30px; writing-mode: vertical-rl; transform: rotate(180deg); font-family: "Roboto", sans-serif; font-size: 9.5px; line-height: 1.3; color: var(--text-soft); font-style: italic; white-space: nowrap; }
  .spine-subtitle strong { font-weight: 700; color: var(--white); }
  .spine-title { position: absolute; left: 12px; top: 280px; writing-mode: vertical-rl; transform: rotate(180deg); font-family: "Anton", sans-serif; font-size: 34px; color: var(--yellow); white-space: nowrap; line-height: 1; }
  .spine-author { position: absolute; left: 0; bottom: 16px; width: 60px; text-align: center; font-family: "Roboto", sans-serif; font-size: 9px; color: var(--yellow); line-height: 1.2; }

  /* front cover */
  .front-cover { position: relative; width: 490px; height: 720px; background: radial-gradient(ellipse at 45% 35%, var(--cover-light), var(--cover) 75%); overflow: hidden; font-family: "Roboto", sans-serif; }
  .author-portrait { position: absolute; left: 0; top: 50px; width: 330px; height: 670px; background: linear-gradient(180deg, #6e625c 0%, #b59281 22%, #d9b3a1 34%, #2a2a2a 52%, #141414 100%); border-radius: 150px 150px 0 0; }
  .author-name { position: absolute; right: 22px; top: 42px; font-size: 17px; color: var(--white); letter-spacing: .5px; }
  .cover-title { position: absolute; right: 22px; top: 72px; display: flex; align-items: center; gap: 4px; font-family: "Anton", sans-serif; font-weight: 400; color: var(--yellow); }
  .paragraph-sign { font-size: 92px; line-height: 1; }
  .title-lines { text-align: right; font-size: 36px; line-height: 1.02; }
  .subtitle { position: absolute; right: 22px; top: 370px; width: 300px; text-align: right; color: var(--white); font-size: 13px; line-height: 1.3; transform: rotate(-5deg); transform-origin: right top; }
  .subtitle .lead { font-family: "Roboto Condensed", sans-serif; font-weight: 700; color: var(--yellow); font-size: 18px; text-transform: uppercase; display: block; }
  .subtitle strong { font-style: italic; font-weight: 700; }
  .tagline { position: absolute; left: 20px; bottom: 30px; width: 440px; color: var(--yellow); font-size: 13px; line-height: 1.4; letter-spacing: .5px; text-align: justify; text-align-last: justify; transform: rotate(-10deg); transform-origin: left bottom; }
</style>
</head>
<body>
<div class="canvas">
  <div class="book">

    <section class="back-cover">
      <div class="back-panel"></div>
      <div class="author-portrait-small" role="img" aria-label="Porträtfoto des Autors im dunklen Anzug vor hellem Hintergrund"></div>
      <div class="brand-name">printvera</div>
      <div class="back-text">
        <p>„Wenn ich in den printvera-Workshops darüber rede, wie viel Sprengkraft im Zusammenspiel von kritischen Klauseln und Formulierungen in kundenseitigen Verträgen und dem Versicherungsschutz eines Unternehmens liegt, können viele der teilnehmenden Führungskräfte anschließend nicht mehr richtig ruhig schlafen.</p>
        <p>Rechtzeitig klug handeln<br>Wie wertvoll ist es für Sie zu erfahren, wo diese Fallstricke in Ihrer betrieblichen Rechtsliteratur lauern und vor allen Dingen, wie diese Zeitbomben entschärft werden?</p>
        <p>„Mein Ziel ist es, dass auch Ihr Unternehmen von unserem jahrelang gewachsenen Know How und dem printvera-Netzwerk aus Fachanwälten für Industrie- und Haftungsrecht profitiert. Dass Sie von betriebswirtschaftlichen Katastrophen aufgrund der Konsequenzen aus „ungünstigen Klauseln und Formulierungen“ bei einer fehlerhaften Produktion verschont bleiben, indem diese präventiv identifiziert werden.“</p>
        <p>Matthias Brenner - Geschäftsführer printvera Beratungs GmbH</p>
      </div>
    </section>

    <section class="spine">
      <div class="spine-subtitle">Einige etwas andere Blicke auf Verträge<br>und Versicherungen der <strong>Druckindustrie</strong></div>
      <div class="spine-title">Rechtzeitig klug handeln</div>
      <div class="spine-author">MATTHIAS<br>BRENNER</div>
    </section>

    <section class="front-cover">
      <div class="author-portrait" role="img" aria-label="Porträtfoto des Autors mit Brille, dunklem Sakko und weißem Hemd, Arme verschränkt"></div>
      <div class="author-name">MATTHIAS BRENNER</div>
      <h1 class="cover-title">
        <span class="paragraph-sign">§</span>
        <span class="title-lines">Rechtzeitig<br>klug<br>handeln</span>
      </h1>
      <p class="subtitle"><span class="lead">Einige etwas anderere Blicke</span>auf Verträge und Versicherungen<br>der <strong>Druckindustrie</strong></p>
      <p class="tagline">Eine Pflichtlektüre für Verantwortliche im Vertrieb und<br>Einkauf und QM des Etiketten- und Verpackungsdrucks</p>
    </section>

  </div>
</div>
</body>
</html>
```